Fun, Clean Business Card For Family Focused Travel Agency

I need a business card using specific colors and fonts as in the uploaded files. Ideally, I would like a large image of the logo on the back and all the contact info on the front. Maybe the stars/dots somewhere in a flowy form.

I do want it the contact information to be clear and easy to read. I don't want it to look too busy. Maybe even a bit minimalist.

I plan or ordering the ROUNDED CORNER business cards from Cardwell Press, so please consider that in your design.

Target Market(s)

Families with children, couples, groups of friends

Contact Information for Business Card

Marla Quent, Owner
Marla@TidewayTrips.example
Cell Phone Number 555-218-6034
Office Phone Number 555-647-1295
Specializing in Fablecrest destinations, Goldmere Parkside Resort, Cruises and All-Inclusive Vacations.

Nice but not required:
www.TidewayTrips.example
Facebook, Instagram, Twitter icons with username: TidewayTrips

Font styles to use
Sans Serif

Requirements
Must have
• Please try to use the colors from the logo as much as possible. I understand lighter shades/colors may be needed for some things.
Should not have
• NO SERIF FONTS. That is really the only thing I do not want at all

```html
<!DOCTYPE html>
<html lang="en">
<head>
<meta charset="utf-8">
<title>Tideway Trips – Business Card</title>
<link rel="stylesheet" href="https://fonts.googleapis.com/css2?family=Damion&family=Ubuntu:wght@300;400;500&display=swap">
<style>
  :root {
    --teal: #2fbb9c;
    --teal-light: #6fd4bd;
    --teal-deep: #22a98a;
    --navy: #2c2e48;
    --paper: #ffffff;
    --backdrop: #eceef0;
    --wash-grey: #e6e7e9;
    --wash-mint: #d7efe8;
    --wash-peach: #f6e3d6;
  }
  * { box-sizing: border-box; margin: 0; padding: 0; }
  html, body { width: 1200px; height: 1064px; overflow: hidden; }
  body {
    background: var(--backdrop);
    font-family: "Ubuntu", sans-serif;
    display: flex;
    flex-direction: column;
    align-items: center;
    justify-content: center;
    gap: 22px;
  }
  .card {
    position: relative;
    width: 880px;
    height: 503px;
    border-radius: 34px;
    overflow: hidden;
    box-shadow: 0 6px 22px rgba(0,0,0,0.08);
  }

  /* Front */
  .card--front { background: var(--paper); }
  .front__name {
    position: absolute;
    left: 70px; top: 48px;
    font-family: "Damion", cursive;
    font-size: 96px;
    line-height: 1;
    color: var(--navy);
  }
  .front__role {
    position: absolute;
    left: 76px; top: 152px;
    font-weight: 300;
    font-size: 34px;
    color: var(--teal);
  }
  .contact-list {
    position: absolute;
    left: 74px; top: 232px;
    list-style: none;
    display: flex;
    flex-direction: column;
    gap: 10px;
  }
  .contact-list__item {
    display: flex;
    align-items: center;
    gap: 18px;
    font-size: 27px;
    color: var(--navy);
  }
  .contact-list__icon { width: 24px; height: 24px; flex: none; }
  .front__art {
    position: absolute;
    right: 40px; bottom: -40px;
    width: 420px; height: 420px;
    border-radius: 50%;
    background: radial-gradient(circle at 55% 45%, var(--wash-grey) 0%, var(--wash-mint) 45%, var(--wash-peach) 70%, rgba(255,255,255,0) 72%);
    opacity: 0.7;
  }

  /* Back */
  .card--back {
    background: linear-gradient(160deg, var(--teal-light) 0%, var(--teal) 45%, var(--teal-deep) 100%);
    display: flex;
    align-items: center;
    justify-content: center;
    gap: 26px;
  }
  .back__dot {
    width: 74px; height: 74px;
    border-radius: 50%;
    background: var(--paper);
  }
  .back__brand {
    font-weight: 500;
    font-size: 84px;
    color: var(--paper);
    letter-spacing: 1px;
  }
</style>
</head>
<body>
  <section class="card card--front">
    <div class="front__art" role="img" aria-label="Faint pastel illustration of a sailing ship on swirling waves with scattered stars and dots"></div>
    <h1 class="front__name">Marla Quent</h1>
    <p class="front__role">Owner</p>
    <ul class="contact-list">
      <li class="contact-list__item">
        <svg class="contact-list__icon" viewBox="0 0 24 24" fill="none" stroke="var(--teal)" stroke-width="1.6"><rect x="7" y="2" width="10" height="20" rx="2"/><line x1="11" y1="18.5" x2="13" y2="18.5"/></svg>
        555-218-6034
      </li>
      <li class="contact-list__item">
        <svg class="contact-list__icon" viewBox="0 0 24 24" fill="var(--teal)"><path d="M9 3c-2 1-4 3-4 6 0 5 4 10 9 12 2 0 3-1 4-2l-3-3-2 1c-2-1-4-4-4-6l1-2-1-6z"/></svg>
        555-647-1295
      </li>
      <li class="contact-list__item">
        <svg class="contact-list__icon" viewBox="0 0 24 24" fill="none" stroke="var(--teal)" stroke-width="1.6"><rect x="2" y="5" width="20" height="14" rx="1"/><polyline points="2,5 12,13 22,5"/></svg>
        Marla@TidewayTrips.example
      </li>
      <li class="contact-list__item">
        <svg class="contact-list__icon" viewBox="0 0 24 24" fill="none" stroke="var(--teal)" stroke-width="1.6"><circle cx="12" cy="12" r="10"/><ellipse cx="12" cy="12" rx="4.5" ry="10"/><line x1="2" y1="12" x2="22" y2="12"/><line x1="4" y1="7" x2="20" y2="7"/><line x1="4" y1="17" x2="20" y2="17"/></svg>
        www.TidewayTrips.example
      </li>
    </ul>
  </section>

  <section class="card card--back">
    <span class="back__dot"></span>
    <span class="back__brand">Tideway Trips</span>
  </section>
</body>
</html>
```